Porchlight Gin - Label for new Gin bottle

I am looking for a bottle label for our small batch, handcrafted Gin. We are located in the bay-side city of Frankston (Victoria, Australia). I know I want more of a serious label but am torn between traditional or modern styling.

Label to include;
• Porchlight GIN (name)
• Hand Crafted
• Small Batch
• 40% Vol

Using 700ml VANTA Spirit Bottle - Cork

Requirements
Must have
• Name; Porchlight Gin
Method: Hand Crafted
Batch Size; Small Batch
Alc; 40% Vol
Nice to have
• Maybe a coastal/seaside reference or reference to distilling.

```html
<!DOCTYPE html>
<html lang="en">
<head>
<meta charset="utf-8">
<title>Porchlight Gin – Bottle Label</title>
<link rel="stylesheet" href="https://fonts.googleapis.com/css2?family=Yellowtail&family=Poppins:wght@500&display=swap">
<style>
  :root {
    --stage: #3a3a3a;
    --label: #2b2b2b;
    --gold: #b8a400;
    --gold-soft: rgba(184, 164, 0, 0.32);
    --ink: #f4f4f4;
  }
  html, body {
    margin: 0;
    width: 1200px;
    height: 675px;
    overflow: hidden;
    background: var(--stage);
  }
  .label {
    position: absolute;
    left: 50px;
    top: 37px;
    width: 1100px;
    height: 600px;
    background: var(--label);
    overflow: hidden;
  }
  .label__rule {
    position: absolute;
    left: 0;
    right: 0;
    height: 6px;
    background: var(--gold);
  }
  .label__rule--top { top: 14px; }
  .label__rule--bottom { bottom: 14px; }
  .label__backdrop {
    position: absolute;
    left: -40px;
    right: -40px;
    top: 70px;
    height: 380px;
    background: linear-gradient(90deg, var(--gold-soft), rgba(184,164,0,0.18) 50%, var(--gold-soft));
    filter: blur(30px);
  }
  .label__brand {
    position: absolute;
    left: 502px;
    top: 120px;
    width: 520px;
    transform: translateX(-50%);
    text-align: center;
  }
  .label__mark {
    display: block;
    width: 96px;
    height: 96px;
    margin: 0 auto 40px;
    background: var(--gold);
  }
  .label__name {
    margin: 0;
    font-family: "Yellowtail", cursive;
    font-weight: 400;
    font-size: 96px;
    line-height: 1;
    color: var(--ink);
  }
  .label__type {
    margin: 2px 0 0;
    padding-right: 86px;
    text-align: right;
    font-family: "Poppins", sans-serif;
    font-weight: 500;
    font-size: 30px;
    line-height: 1;
    letter-spacing: 1px;
    color: var(--ink);
  }
  .label__facts {
    position: absolute;
    top: 512px;
    left: 0;
    right: 0;
    height: 50px;
    color: var(--ink);
  }
  .fact {
    position: absolute;
    top: 0;
    font-family: "Yellowtail", cursive;
    font-size: 38px;
    line-height: 50px;
    white-space: nowrap;
    transform: translateX(-50%);
  }
  .fact--batch { left: 216px; }
  .fact--craft { left: 512px; }
  .fact--abv {
    left: 792px;
    font-family: "Poppins", sans-serif;
    font-size: 24px;
  }
  .fact-dot {
    position: absolute;
    top: 20px;
    width: 11px;
    height: 11px;
    background: var(--ink);
    border-radius: 50%;
    transform: translateX(-50%);
  }
  .fact-dot--one { left: 357px; }
  .fact-dot--two { left: 676px; }
</style>
</head>
<body>
  <main class="label">
    <div class="label__rule label__rule--top"></div>
    <div class="label__backdrop" role="img" aria-label="Large soft blurred gold script lettering of the brand name behind the title"></div>
    <div class="label__brand">
      <span class="label__mark" aria-hidden="true"></span>
      <h1 class="label__name">Porchlight</h1>
      <p class="label__type">GIN</p>
    </div>
    <div class="label__facts">
      <span class="fact fact--batch">Small Batch</span>
      <span class="fact-dot fact-dot--one"></span>
      <span class="fact fact--craft">Hand Crafted</span>
      <span class="fact-dot fact-dot--two"></span>
      <span class="fact fact--abv">40% Vol</span>
    </div>
    <div class="label__rule label__rule--bottom"></div>
  </main>
</body>
</html>
```